Clean professional design needed for landscape property business

We need a logo for a new lawncare, landscaping , property maintenance business called Meadow Trim.
Our services include lawn mowing, garden maintenance, clean ups and some property maintenance.
We want a double sided business card that is clean and very professional using the colour scheme from our logo which is provided.
the business card should have impact as we will use these to drop into people's letterboxes as a marketing drop.
Initially we want to see what you come up with so there is a very wide scope here to work with.
Updates

Project Deadline Extended
Reason: we feel our original deadline was too short. we have extended to give more time for quality submissions.

Target Market(s)

High end property owners who don't wish to do there own gardneing or property maintenance

Industry/Entity Type

Business

Contact Information for Business Card

Name
Postion/ Title
Phone number
mobile
web address
physical address

services offered

Font styles to use
Sans Serif

Requirements
Must have
• curved edges preferrred
Nice to have
• We like the idea of the logo being embossed or etched into the card so it looks like it is below the surface of the card
Should not have
• No stock images or characters.

```html
<!DOCTYPE html>
<html lang="en">
<head>
<meta charset="utf-8">
<title>Meadow Trim – Business Card, Front and Back</title>
<link href="https://fonts.googleapis.com/css2?family=Lato:wght@400;700&family=Montserrat:wght@400;600;800&display=swap" rel="stylesheet">
<style>
  :root {
    --backdrop: #d9d9d8;
    --card: #f4f4f2;
    --ink: #3a3b3d;
    --green: #6fb43f;
    --band: #3e3f42;
    --strip: #7aab43;
    --rule: #4a4b4d;
  }
  * { margin: 0; padding: 0; box-sizing: border-box; }
  html, body { width: 960px; height: 1200px; overflow: hidden; }
  body { background: var(--backdrop); font-family: "Lato", sans-serif; color: var(--ink); position: relative; }

  .side { position: absolute; left: 0; width: 960px; display: flex; align-items: center; justify-content: center; }
  .side--front { top: 0; height: 525px; }
  .side--back { top: 635px; height: 512px; }

  .card {
    width: 560px; height: 320px; background: var(--card);
    border-radius: 28px; position: relative;
    box-shadow: 0 3px 0 #c9c9c7, 0 10px 24px rgba(0,0,0,.12);
  }

  .brand { display: flex; align-items: center; gap: 14px; font-family: "Montserrat", sans-serif; font-weight: 800; color: var(--green); }
  .brand__dot { width: 34px; height: 34px; border-radius: 50%; background: var(--green); flex: none; }

  .card--front .brand { position: absolute; left: 58px; top: 110px; font-size: 50px; letter-spacing: -1px; }
  .card--front .address { position: absolute; left: 60px; top: 200px; font-size: 17px; }

  .card--back .person { position: absolute; left: 44px; top: 44px; font-family: "Montserrat", sans-serif; }
  .person__name { font-size: 30px; font-weight: 800; letter-spacing: 1px; }
  .person__name span { color: var(--green); }
  .person__role { font-size: 17px; letter-spacing: 1.5px; margin-top: 2px; }

  .contacts { position: absolute; left: 44px; top: 132px; list-style: none; font-size: 14px; line-height: 19px; }
  .contacts li { display: flex; align-items: center; gap: 8px; }
  .contacts svg { width: 12px; height: 12px; flex: none; }

  .divider { position: absolute; left: 44px; right: 44px; top: 202px; height: 1.5px; background: var(--rule); }

  .card--back .brand { position: absolute; left: 44px; top: 234px; font-size: 24px; gap: 10px; }
  .card--back .brand__dot { width: 22px; height: 22px; }

  .services { position: absolute; right: 44px; top: 218px; list-style: none; font-size: 14px; line-height: 20px; text-align: left; }

  .label-band {
    position: absolute; left: 0; top: 525px; width: 958px; height: 110px;
    background: var(--band); color: #fff; display: flex; align-items: center; justify-content: center;
    font-size: 45px; font-weight: 400;
  }
  .footer-strip { position: absolute; left: 0; top: 1147px; width: 960px; height: 53px; background: var(--strip); }
</style>
</head>
<body>
  <section class="side side--front">
    <article class="card card--front">
      <div class="brand"><span>Meadow Trim</span><span class="brand__dot"></span></div>
      <p class="address">412 Larkspur Lane, Brookfield, PA 18210</p>
    </article>
  </section>

  <div class="label-band">Front and Back Side</div>

  <section class="side side--back">
    <article class="card card--back">
      <div class="person">
        <p class="person__name">SAM <span>ELLIS</span></p>
        <p class="person__role">MANAGER</p>
      </div>
      <ul class="contacts">
        <li><svg viewBox="0 0 12 12"><circle cx="6" cy="6" r="6" fill="#6fb43f"/><path d="M4 3.5l1 1.6-.6.6a4 4 0 0 0 1.9 1.9l.6-.6 1.6 1-.6 1C5.8 9 3 6.2 3 4.1z" fill="#fff"/></svg>+12 123 456 7890</li>
        <li><svg viewBox="0 0 12 12"><circle cx="6" cy="6" r="6" fill="#6fb43f"/><rect x="3" y="4" width="6" height="4.2" fill="none" stroke="#fff" stroke-width="0.9"/><path d="M3 4l3 2.4L9 4" fill="none" stroke="#fff" stroke-width="0.9"/></svg>youremail@domain.com</li>
        <li><svg viewBox="0 0 12 12"><circle cx="6" cy="6" r="6" fill="#6fb43f"/><circle cx="6" cy="6" r="3" fill="none" stroke="#fff" stroke-width="0.9"/><path d="M3 6h6M6 3v6" stroke="#fff" stroke-width="0.8"/></svg>www.yoursite.com</li>
      </ul>
      <div class="divider"></div>
      <div class="brand"><span>Meadow Trim</span><span class="brand__dot"></span></div>
      <ul class="services">
        <li>First service goes here</li>
        <li>Second Service here</li>
        <li>Third Service here</li>
      </ul>
    </article>
  </section>

  <div class="footer-strip"></div>
</body>
</html>
```